Vok Social Network Needs Web Front

Vok needs a web front end to describe its vision, put out blog articles for our new California startup. Vok is a Social Network and Social Media Application which starts with the idea that we all do good things. Take for instance yourself, while many may call you a graphic artists and design genius, at your core, what you enjoy about what you do is “creating opportunity” for ideas and businesses to excel.

We want to first appeal to every day people - college students, parents, retail professionals but be attractive to volunteers, philanthropists and spiritual organizations.

Instead of limiting colors and design style, I will provide our logo and our mobile profile screen. Please take this as inspiration (feel free not to let our existing style limit yours).

The final design should communicate social network/mobile/software genius.

Industry/Entity Type

Media

```html
<!DOCTYPE html>
<html lang="en">
<head>
<meta charset="utf-8">
<title>Vok — Social Network and Social Media Application</title>
<link href="https://fonts.googleapis.com/css2?family=Oswald:wght@400;500;700&family=Open+Sans:wght@400;600;700&display=swap" rel="stylesheet">
<style>
:root{
  --red:#c1272d;
  --ink:#1d1d1d;
  --text:#555555;
  --muted:#8a8a8a;
  --light:#f0f0f0;
  --line:#d8d8d8;
  --white:#ffffff;
}
*{box-sizing:border-box;margin:0;padding:0}
html,body{width:1200px;height:3068px;overflow:hidden}
body{position:relative;background:var(--white);font-family:"Open Sans",Arial,sans-serif;color:var(--text)}
h1,h2,h3,.brand,.nav a,.btn{font-family:"Oswald","Arial Narrow",sans-serif}

/* Hero */
.hero{position:absolute;left:0;top:0;width:1200px;height:688px;overflow:hidden;
  background:radial-gradient(ellipse at 70% 55%,#4a4a4a 0%,#2b2b2b 45%,#151515 100%)}
.hero-bg{position:absolute;inset:0}
.hero-photo{position:absolute;left:740px;top:180px;width:420px;height:508px;
  background:linear-gradient(160deg,#3a3a3a 0%,#1e1e1e 55%,#b08e78 100%);opacity:.85;border-radius:40px 40px 0 0}
.brand{position:absolute;color:var(--white);font-weight:700;font-size:40px;letter-spacing:1px}
.hero .brand{left:80px;top:28px}
.nav{position:absolute;left:720px;top:50px;display:flex;gap:28px}
.nav a{color:#d0d0d0;text-decoration:none;font-size:13px;letter-spacing:.5px}
.nav a.active{color:var(--red)}
.hero h1{position:absolute;left:152px;top:258px;color:var(--white);font-size:32px;font-weight:500;letter-spacing:.5px}
.hero-lead{position:absolute;left:152px;top:310px;width:360px;color:#cfcfcf;font-size:14px;line-height:22px}
.btn{position:absolute;display:flex;align-items:center;justify-content:center;color:var(--white);font-size:13px;letter-spacing:1px;height:44px;border-radius:2px}
.btn-red{background:var(--red)}
.btn-gray{background:#4a4a4a}
.slider-arrow{position:absolute;top:352px}

/* About */
.section-title{position:absolute;left:0;width:1200px;text-align:center;color:var(--ink);font-size:30px;font-weight:500;letter-spacing:.5px}
.section-sub{position:absolute;left:350px;width:500px;text-align:center;font-size:13px;line-height:21px;color:var(--text)}
.feature{position:absolute;width:300px}
.feature svg{display:block;margin-bottom:14px}
.feature h3{font-family:"Open Sans",Arial,sans-serif;font-size:20px;font-weight:600;color:var(--ink);margin-bottom:10px}
.feature h3 span{color:var(--red)}
.feature p{font-size:12px;line-height:19px;color:var(--text)}
.device{position:absolute;left:484px;top:862px;width:252px;height:440px;border-radius:34px;background:#e6e6e6;border:2px solid #cfcfcf}
.device-screen{position:absolute;left:18px;top:62px;width:212px;height:316px;background:linear-gradient(180deg,#2a2a2a,#0e0e0e)}

/* Blog */
.blog{position:absolute;left:0;top:1320px;width:1200px;height:640px;background:var(--light)}
.card{position:absolute;top:180px;width:304px}
.card-img{width:304px;height:252px;background:linear-gradient(160deg,#d9d3cb 0%,#b49a86 50%,#6f6a66 100%)}
.card h3{font-family:"Oswald","Arial Narrow",sans-serif;font-size:14px;font-weight:500;color:var(--ink);line-height:20px;margin-top:14px}
.meta{display:flex;gap:20px;margin-top:8px;font-size:11px;color:var(--muted);align-items:center}
.meta span{display:flex;align-items:center;gap:6px}
.card p{margin-top:10px;font-size:11px;line-height:17px;color:var(--text)}

/* Subscribe */
.subscribe{position:absolute;left:0;top:1960px;width:1200px;height:312px;background:linear-gradient(180deg,#1f1f1f,#141414)}
.subscribe h2{position:absolute;left:0;top:52px;width:1200px;text-align:center;color:var(--white);font-size:30px;font-weight:500}
.subscribe p{position:absolute;left:340px;top:110px;width:520px;text-align:center;color:#bdbdbd;font-size:13px;line-height:21px}
.field-dark{position:absolute;left:370px;top:210px;width:316px;height:48px;border:1px solid #4a4a4a;background:#181818;color:#9a9a9a;font-size:13px;padding:14px 18px}
.subscribe .btn{left:696px;top:210px;width:132px;height:48px}

/* Contact */
.field{position:absolute;border:1px solid var(--line);background:var(--white);font-size:12px;color:#9a9a9a;padding:14px 16px}
.contact .btn{left:490px;top:2676px;width:188px;height:56px;font-size:15px}

/* Footer */
.footer{position:absolute;left:0;top:2788px;width:1200px;height:280px;background:linear-gradient(180deg,#1d1d1d,#111111)}
.footer .brand{left:0;width:1200px;text-align:center;top:38px;font-size:48px}
.social{position:absolute;left:0;top:172px;width:1200px;display:flex;justify-content:center;gap:22px}
.social span{width:26px;height:26px;border-radius:50%;background:#e6e6e6;display:block}
.copyright{position:absolute;left:0;top:234px;width:1200px;text-align:center;font-size:12px;color:#a0a0a0}
</style>
</head>
<body>

<header class="hero">
  <div class="hero-bg" role="img" aria-label="Dark blurred background photograph"></div>
  <div class="hero-photo" role="img" aria-label="Photograph of a hand holding a smartphone showing the app screen"></div>
  <div class="brand">Vok</div>
  <nav class="nav">
    <a class="active" href="#">HOME</a>
    <a href="#">DOWNLOAD</a>
    <a href="#">PHOTO GALLERY</a>
    <a href="#">VIDEOS</a>
    <a href="#">CONTACT</a>
  </nav>
  <svg class="slider-arrow" style="left:34px" width="20" height="32" viewBox="0 0 20 32"><path d="M15 4 5 16l10 12" fill="none" stroke="#9a9a9a" stroke-width="3"/></svg>
  <svg class="slider-arrow" style="left:1146px" width="20" height="32" viewBox="0 0 20 32"><path d="M5 4l10 12L5 28" fill="none" stroke="#9a9a9a" stroke-width="3"/></svg>
  <h1>THE IDEA THAT WE ALL DO GOOD THINGS</h1>
  <p class="hero-lead">Lumora is a Responsive and Modern Mobile App Landing Page. Lorem ipsum dolor sit amet, consectetur adipiscing elit, sed do eiusmod tempor.</p>
  <div class="btn btn-red" style="left:152px;top:410px;width:160px">LEARN MORE</div>
  <div class="btn btn-gray" style="left:336px;top:410px;width:160px">DOWNLOAD NOW</div>
</header>

<section class="about">
  <h2 class="section-title" style="top:728px">VOK IS A SOCIAL NETWORK AND SOCIAL MEDIA APPLICATION</h2>
  <p class="section-sub" style="top:796px">Lorem ipsum dolor sit amet, consectetur adipiscing elit, sed do eiusmod tempor incididunt ut labore et dolore magna aliqua.</p>

  <div class="feature" style="left:152px;top:884px">
    <svg width="28" height="24" viewBox="0 0 28 24"><rect x="2" y="2" width="24" height="15" fill="none" stroke="#333" stroke-width="2"/><path d="M10 22h8M14 17v5" stroke="#333" stroke-width="2"/></svg>
    <h3><span>Social</span> media</h3>
    <p>Ipsum factorial non deposit quid pro quo hic escorol. Olypian quarrels et gorilla congolium sic ad nauseum.</p>
  </div>
  <div class="feature" style="left:152px;top:1090px">
    <svg width="28" height="24" viewBox="0 0 28 24"><rect x="2" y="2" width="24" height="15" fill="none" stroke="#333" stroke-width="2"/><circle cx="14" cy="9.5" r="3" fill="#333"/><path d="M10 22h8M14 17v5" stroke="#333" stroke-width="2"/></svg>
    <h3><span>Social</span> Network</h3>
    <p>Ipsum factorial non deposit quid pro quo hic escorol. Olypian quarrels et gorilla congolium sic ad nauseum.</p>
  </div>

  <div class="device">
    <div class="device-screen" role="img" aria-label="App profile screen shown on the phone"></div>
  </div>

  <div class="feature" style="left:804px;top:884px">
    <svg width="26" height="24" viewBox="0 0 26 24"><path d="M3 10h5v12H3zM8 11l5-9c2 0 3 1 3 3l-1 5h7c1.5 0 2.5 1.2 2.2 2.6l-1.8 8c-.3 1.2-1.2 2.4-2.6 2.4H8" fill="none" stroke="#333" stroke-width="2" stroke-linejoin="round"/></svg>
    <h3><span>Free</span> Support</h3>
    <p>Ipsum factorial non deposit quid pro quo hic escorol. Olypian quarrels et gorilla congolium sic ad nauseum.</p>
  </div>
  <div class="feature" style="left:804px;top:1090px">
    <svg width="26" height="24" viewBox="0 0 26 24"><rect x="2" y="2" width="22" height="20" rx="2" fill="none" stroke="#333" stroke-width="2"/><path d="M10 8l-4 4 4 4M16 8l4 4-4 4" fill="none" stroke="#333" stroke-width="2"/></svg>
    <h3><span>Clean</span> Code</h3>
    <p>Ipsum factorial non deposit quid pro quo hic escorol. Olypian quarrels et gorilla congolium sic ad nauseum.</p>
  </div>
</section>

<section class="blog">
  <h2 class="section-title" style="top:44px">BLOG ARTICLES</h2>
  <p class="section-sub" style="top:100px;left:300px;width:600px">Hac consectetur et Phasellus dignissim, urna a iaculis scelerisque, nulla purus pharetra eros, sed vulputate nisl erat ut amet nisi. Praesent vestibulum tellus.</p>

  <article class="card" style="left:100px">
    <div class="card-img" role="img" aria-label="Photograph of a young woman using her phone"></div>
    <h3>CURABITUR VULPUTATE LIBERO A AUSTO POSUERE, AC ULLAMCORPER SEM IMPERDIET.</h3>
    <div class="meta">
      <span><svg width="10" height="10" viewBox="0 0 10 10"><rect x="1" y="2" width="8" height="7" fill="none" stroke="#8a8a8a"/><path d="M1 4h8" stroke="#8a8a8a"/></svg>30/08/15</span>
      <span><svg width="11" height="10" viewBox="0 0 11 10"><path d="M1 1h9v6H5L2 9V7H1z" fill="none" stroke="#8a8a8a"/></svg>12 COMMENTS</span>
    </div>
    <p>Phasellus dignissim, urna a iaculis scelerisque, nulla purus pharetra eros, sed vulputate nisl erat ut amet. Praesent vestibulum tellus at tellus semper.</p>
  </article>

  <article class="card" style="left:448px">
    <div class="card-img" role="img" aria-label="Photograph of a young woman reading on a tablet"></div>
    <h3>CURABITUR VULPUTATE LIBERO A AUSTO POSUERE, AC ULLAMCORPER SEM IMPERDIET.</h3>
    <div class="meta">
      <span><svg width="10" height="10" viewBox="0 0 10 10"><rect x="1" y="2" width="8" height="7" fill="none" stroke="#8a8a8a"/><path d="M1 4h8" stroke="#8a8a8a"/></svg>30/08/15</span>
      <span><svg width="11" height="10" viewBox="0 0 11 10"><path d="M1 1h9v6H5L2 9V7H1z" fill="none" stroke="#8a8a8a"/></svg>12 COMMENTS</span>
    </div>
    <p>Phasellus dignissim, urna a iaculis scelerisque, nulla purus pharetra eros, sed vulputate nisl erat ut amet. Praesent vestibulum tellus at tellus semper.</p>
  </article>

  <article class="card" style="left:792px">
    <div class="card-img" role="img" aria-label="Photograph of a young woman texting on her phone"></div>
    <h3>CURABITUR VULPUTATE LIBERO A AUSTO POSUERE, AC ULLAMCORPER SEM IMPERDIET.</h3>
    <div class="meta">
      <span><svg width="10" height="10" viewBox="0 0 10 10"><rect x="1" y="2" width="8" height="7" fill="none" stroke="#8a8a8a"/><path d="M1 4h8" stroke="#8a8a8a"/></svg>30/08/15</span>
      <span><svg width="11" height="10" viewBox="0 0 11 10"><path d="M1 1h9v6H5L2 9V7H1z" fill="none" stroke="#8a8a8a"/></svg>12 COMMENTS</span>
    </div>
    <p>Phasellus dignissim, urna a iaculis scelerisque, nulla purus pharetra eros, sed vulputate nisl erat ut amet. Praesent vestibulum tellus at tellus semper.</p>
  </article>
</section>

<section class="subscribe">
  <h2>SUBSCRIBE TO LUMORA</h2>
  <p>Praesent commodo cursus magna, vel scelerisque nisl consectetur et Phasellus dignissim, urna a iaculis scelerisque, nulla purus pharetra eros, sed vulputate nisl erat sit amet nisi. Praesent vestibulum tellus et tellus semper.</p>
  <div class="field-dark">Enter your Email...</div>
  <div class="btn btn-red">Subscribe</div>
</section>

<section class="contact">
  <h2 class="section-title" style="top:2296px">CONTACT LUMORA APP</h2>
  <p class="section-sub" style="top:2346px">Factorial non deposit quid pro quo hic escorol. Olypian quarrels et gorilla congolium sic ad nauseum.</p>
  <div class="field" style="left:160px;top:2412px;width:400px;height:56px">YOUR NAME*</div>
  <div class="field" style="left:160px;top:2508px;width:400px;height:56px">YOUR EMAIL*</div>
  <div class="field" style="left:160px;top:2604px;width:400px;height:56px">YOUR PHONE*</div>
  <div class="field" style="left:612px;top:2412px;width:460px;height:248px">YOUR MESSAGE*</div>
  <div class="btn btn-red">SEND MASSAGE</div>
</section>

<footer class="footer">
  <div class="brand">Vok</div>
  <div class="social" aria-label="Social links">
    <span></span><span></span><span></span><span></span><span></span><span></span><span></span><span></span>
  </div>
  <p class="copyright">© Vok 2014 All rights reserved</p>
</footer>

</body>
</html>
```